Business Card for Canvas & Calm-Eco Friendly Organic Clothing Brand

We are looking for an amazing business card for our eco friendly, organic clothing brand. We are thinking maybe a business card with a peel off sticker on the back, since our hanging clothing tag is a peel off sticker on the back. I will attach our hang tag so we can make sure we stay in line with our design. I've also attached a bag we are doing because I do like the scattered emblem look as well.

```html
<!DOCTYPE html>
<html lang="en">
<head>
<meta charset="utf-8">
<title>Canvas &amp; Calm – Business Card</title>
<link href="https://fonts.googleapis.com/css2?family=Arimo:wght@400;700&display=swap" rel="stylesheet">
<style>
  :root {
    --page-bg: #d9d9d9;
    --card-white: #ffffff;
    --card-black: #0c0c0c;
    --gold: #c9a13b;
    --gold-light: #ecd48a;
    --gold-dark: #8a6a1e;
    --ink: #3a3a3a;
    --ink-soft: #555555;
  }
  * { margin: 0; padding: 0; box-sizing: border-box; }
  html, body { width: 1200px; height: 950px; overflow: hidden; }
  body {
    background: var(--page-bg);
    font-family: "Arimo", Arial, sans-serif;
    position: relative;
  }
  .card {
    position: absolute;
    left: 250px;
    width: 700px;
    height: 400px;
    box-shadow: 0 6px 18px rgba(0,0,0,0.18);
    overflow: hidden;
  }
  .card--front { top: 50px; background: var(--card-white); }
  .card--back { top: 500px; background: var(--card-black); }

  /* Front */
  .brand {
    position: absolute;
    left: 48px;
    top: 56px;
    display: flex;
    align-items: center;
    gap: 14px;
  }
  .brand__square {
    width: 30px; height: 30px;
    background: var(--gold);
  }
  .brand__name {
    font-size: 34px;
    font-weight: 700;
    color: var(--gold);
    letter-spacing: 0.5px;
  }
  .contact {
    position: absolute;
    left: 48px;
    top: 176px;
    font-size: 19px;
    color: var(--ink);
    line-height: 25px;
  }
  .contact__row { display: flex; align-items: center; gap: 8px; }
  .contact__icon { width: 16px; height: 16px; flex: none; }
  .contact__address { padding-left: 0; }
  .person {
    position: absolute;
    right: 84px;
    bottom: 56px;
    text-align: left;
  }
  .person__name {
    font-size: 24px;
    font-weight: 700;
    color: var(--ink);
    letter-spacing: 0.5px;
  }
  .person__title {
    font-size: 18px;
    color: var(--ink-soft);
    letter-spacing: 1px;
  }
  .gold-tab {
    position: absolute;
    right: 32px;
    bottom: 52px;
    width: 22px;
    height: 52px;
    background: linear-gradient(90deg, var(--gold-dark), var(--gold-light), var(--gold));
  }

  /* Back */
  .back-pattern {
    position: absolute;
    inset: 0;
    background: radial-gradient(ellipse at 50% 40%, #222 0%, #111 55%, #050505 100%);
  }
  .sticker {
    position: absolute;
    left: 170px;
    top: 120px;
    width: 360px;
    height: 120px;
    border: 4px solid var(--gold);
    border-radius: 12px;
    background: #0a0a0a;
    box-shadow: 0 0 0 2px #000 inset;
  }
  .sticker__emblems {
    position: absolute;
    left: 18px; top: 18px; right: 18px; bottom: 18px;
    border-radius: 6px;
    background: linear-gradient(90deg, #1a1408, #5a4515 30%, #2a200b 60%, #5a4515 85%, #1a1408);
  }
  .back-web {
    position: absolute;
    left: 0; right: 0;
    top: 268px;
    text-align: center;
    font-size: 18px;
    color: #bdbdbd;
    letter-spacing: 2px;
  }
</style>
</head>
<body>

<section class="card card--front" aria-label="Business card front">
  <div class="brand">
    <span class="brand__square"></span>
    <span class="brand__name">Canvas &amp; Calm</span>
  </div>

  <div class="contact">
    <div class="contact__address">2170 Harbor Lane</div>
    <div class="contact__address">Cedar Point, NY 11520</div>
    <div class="contact__row">
      <svg class="contact__icon" viewBox="0 0 16 16"><path fill="#c9a13b" d="M3 2h3l1 3-2 1.5a8 8 0 0 0 4.5 4.5L11 9l3 1v3a1 1 0 0 1-1 1A11 11 0 0 1 2 3a1 1 0 0 1 1-1z"/></svg>
      <span>555 0148 2290</span>
    </div>
    <div class="contact__row">
      <svg class="contact__icon" viewBox="0 0 16 16"><rect x="4" y="1" width="8" height="14" rx="1.5" fill="#c9a13b"/><rect x="5.5" y="3" width="5" height="8" fill="#fff"/></svg>
      <span>555 0173 6614</span>
    </div>
    <div class="contact__row">
      <svg class="contact__icon" viewBox="0 0 16 16"><rect x="4" y="1" width="8" height="5" fill="#c9a13b"/><rect x="1" y="6" width="14" height="7" rx="1" fill="#c9a13b"/><rect x="4" y="10" width="8" height="5" fill="#fff" stroke="#c9a13b"/></svg>
      <span>555 0192 4037</span>
    </div>
    <div class="contact__row">
      <svg class="contact__icon" viewBox="0 0 16 16"><rect x="1" y="3" width="14" height="10" fill="#c9a13b"/><path d="M1 3l7 6 7-6" fill="none" stroke="#fff" stroke-width="1.2"/></svg>
      <span>hello@canvascalm.com</span>
    </div>
  </div>

  <div class="person">
    <div class="person__name">MARK ELLISON</div>
    <div class="person__title">PRESIDENT</div>
  </div>
  <div class="gold-tab"></div>
</section>

<section class="card card--back" aria-label="Business card back">
  <div class="back-pattern" role="img" aria-label="Faint scattered pattern of peace words, hearts and emblems on black"></div>
  <div class="sticker">
    <div class="sticker__emblems" role="img" aria-label="Row of gold emblems: meditating figure, heart, peace symbol and hand sign"></div>
  </div>
  <div class="back-web">www.canvascalm.com</div>
</section>

</body>
</html>
```